Brevard's Jewelers Big Sale

Brevard's Jewelers is an independent fine store in Fort Worth, Texas. We have been in business since 1893 and we only have one sale per year. This is our 120th year. Our stores are upscale and our one sale is similar to a Corwin Tallis Final Round.

we need to include:
up to 60% off
diamonds, watches, fashion designer jewelry and gifts
sale dates April 4th through April 13th
all sales are final
*we are sorry, but Vantor and Mirelle are not included.

Reason: We like some of the designs, but we are still looking for a great headline or name for the sale. thanks!

Requirements
Must have
• must show our logo, which is in the uploaded file.

we also need to list our stores:
Downtown, Oak and 5th St. 555-214-7093
4317 Elmsford Ridge Rd, 555-862-3147
Pinecrest Commons, 555-379-5026
Silverbrook Village Plaza, 555-640-1958
Nice to have
• We would like a catchy tag line that will look good in color print, black and white newspaper and billboard.
Should not have
• We do not want a high impact, low-end sale look.

```html
<!DOCTYPE html>
<html lang="en">
<head>
<meta charset="utf-8">
<title>Brevard's Jewelers – Final Chance End of Season Sale</title>
<link rel="stylesheet" href="https://fonts.googleapis.com/css2?family=Cinzel:wght@400&family=Quicksand:wght@300;400;700&display=swap">
<style>
  :root {
    --plum: #4a1a5e;
    --plum-deep: #3b0c55;
    --paper: #ffffff;
    --stage: #ebe7e1;
    --white: #ffffff;
  }
  * { margin: 0; padding: 0; box-sizing: border-box; }
  html, body { width: 960px; height: 1200px; overflow: hidden; }
  body { background: var(--stage); position: relative; }

  .flyer {
    position: absolute; left: 16px; top: 0;
    width: 928px; height: 1200px;
    background: var(--paper);
    overflow: hidden;
  }
  .flyer-photo {
    position: absolute; inset: 0;
    background:
      radial-gradient(ellipse 300px 110px at 430px 870px, rgba(140, 80, 190, 0.35), rgba(140, 80, 190, 0) 70%),
      linear-gradient(180deg, #ffffff 0%, #f4f3f6 40%, #e7e5ea 62%, #f6f5f7 78%, #ffffff 100%);
  }

  .brand-name {
    position: absolute; top: 92px; left: 0; width: 100%;
    text-align: center; white-space: nowrap;
    font-family: "Cinzel", serif; font-weight: 400;
    font-size: 40px; letter-spacing: 2px;
    color: var(--plum-deep);
  }

  .headline {
    position: absolute; top: 282px; left: 0; width: 100%;
    text-align: center; white-space: nowrap;
    font-family: "Cinzel", serif; font-weight: 400;
    font-size: 68px; line-height: 1; letter-spacing: 2px;
    color: var(--plum);
  }
  .subhead {
    position: absolute; top: 362px; left: 164px; width: 616px;
    text-align: center; white-space: nowrap;
    font-family: "Cinzel", serif; font-weight: 400;
    font-size: 20px; line-height: 24px;
    letter-spacing: 17px; padding-left: 17px;
    color: var(--plum);
  }
  .tagline-band {
    position: absolute; top: 397px; left: 164px;
    width: 616px; height: 45px;
    background: var(--plum-deep);
    display: flex; align-items: center; justify-content: center;
    white-space: nowrap;
    font-family: "Cinzel", serif; font-weight: 400;
    font-size: 23px; letter-spacing: 10px; padding-left: 10px;
    color: var(--white);
  }

  .offer {
    position: absolute; top: 532px; left: 57px;
    font-family: "Quicksand", sans-serif; color: var(--plum);
  }
  .offer-amount { font-size: 76px; font-weight: 300; line-height: 1; letter-spacing: 2px; white-space: nowrap; }
  .offer-details { margin-top: 10px; font-size: 27px; font-weight: 400; line-height: 37px; white-space: nowrap; }

  .exclusion {
    position: absolute; top: 1056px; right: 15px;
    white-space: nowrap;
    font-family: "Quicksand", sans-serif; font-weight: 700;
    font-size: 18px; letter-spacing: 0.5px;
    color: var(--plum);
  }

  .store-list {
    position: absolute; left: 0; bottom: 0;
    width: 100%; height: 96px;
    background: var(--plum-deep);
    display: grid; grid-template-columns: 473px 1fr;
    padding: 18px 0 0 28px; row-gap: 12px;
    list-style: none;
    font-family: "Quicksand", sans-serif; font-weight: 700;
    font-size: 16px; letter-spacing: 0.6px;
    color: var(--white);
  }
  .store { display: flex; align-items: center; gap: 12px; height: 24px; white-space: nowrap; }
  .store svg { width: 16px; height: 22px; flex: none; }
</style>
</head>
<body>
  <main class="flyer">
    <div class="flyer-photo" role="img" aria-label="Soft-focus photo of a silver pendant with an oval amethyst flanked by small diamonds on a white surface"></div>

    <div class="brand-name">BREVARD'S JEWELERS</div>

    <h1 class="headline">FINAL CHANCE</h1>
    <p class="subhead">END OF SEASON SALE</p>
    <p class="tagline-band">NOW. ELSE 365 DAYS LATER</p>

    <section class="offer">
      <p class="offer-amount">Up to 60% off</p>
      <p class="offer-details">
        Diamonds, watches, fashion designer jewelry and gifts<br>
        Sale dates April 4th through April 13th<br>
        All sales are final
      </p>
    </section>

    <p class="exclusion">*We are sorry, but Vantor and Mirelle are not included.</p>

    <ul class="store-list">
      <li class="store">
        <svg viewBox="0 0 16 22" aria-hidden="true"><path fill="#fff" d="M8 0C3.6 0 0 3.5 0 7.9 0 13.5 8 22 8 22s8-8.5 8-14.1C16 3.5 12.4 0 8 0zm0 11a3.2 3.2 0 1 1 0-6.4A3.2 3.2 0 0 1 8 11z"/></svg>
        Downtown, Oak and 5th St. 555-214-7093
      </li>
      <li class="store">
        <svg viewBox="0 0 16 22" aria-hidden="true"><path fill="#fff" d="M8 0C3.6 0 0 3.5 0 7.9 0 13.5 8 22 8 22s8-8.5 8-14.1C16 3.5 12.4 0 8 0zm0 11a3.2 3.2 0 1 1 0-6.4A3.2 3.2 0 0 1 8 11z"/></svg>
        4317 Elmsford Ridge Rd, 555-862-3147
      </li>
      <li class="store">
        <svg viewBox="0 0 16 22" aria-hidden="true"><path fill="#fff" d="M8 0C3.6 0 0 3.5 0 7.9 0 13.5 8 22 8 22s8-8.5 8-14.1C16 3.5 12.4 0 8 0zm0 11a3.2 3.2 0 1 1 0-6.4A3.2 3.2 0 0 1 8 11z"/></svg>
        Pinecrest Commons, 555-379-5026
      </li>
      <li class="store">
        <svg viewBox="0 0 16 22" aria-hidden="true"><path fill="#fff" d="M8 0C3.6 0 0 3.5 0 7.9 0 13.5 8 22 8 22s8-8.5 8-14.1C16 3.5 12.4 0 8 0zm0 11a3.2 3.2 0 1 1 0-6.4A3.2 3.2 0 0 1 8 11z"/></svg>
        Silverbrook Village Plaza, 555-640-1958
      </li>
    </ul>
  </main>
</body>
</html>
```